Small Business Consulting Firm Needs Business Card Design

Need a sleek modern business card with 2 sides matching the colors of our logo. We will be placing these with a mailer we are sending out. These business cards will only ever be given to business owners. We operate helping businesses who are struggling with cash flow or finances. If the green and blue design needs to be moved to the right of "Harborline Crest Consulting" for aesthetic purposes that is ok. We will need an editable file if possible. We would like to include the reps name, email, website, and phone number. For now just use Peter Vance, pvance@harborlinecrest.com, www.harborlinecrest.com, and 833-555-0172.

```html
<!DOCTYPE html>
<html lang="en">
<head>
<meta charset="UTF-8">
<title>Harborline Crest Consulting – Business Card</title>
<link rel="stylesheet" href="https://fonts.googleapis.com/css2?family=Montserrat:wght@300;400&display=swap">
<style>
  :root {
    --paper: #ffffff;
    --card-edge: #d2d2d2;
    --ink: #454545;
    --brand-green: #79bb43;
    --brand-green-deep: #639e36;
    --brand-blue: #0080c6;
  }
  * { margin: 0; padding: 0; box-sizing: border-box; }
  html, body {
    width: 960px;
    height: 1200px;
    overflow: hidden;
    background: var(--paper);
    font-family: "Montserrat", Arial, sans-serif;
    color: var(--ink);
  }
  .sheet { position: relative; width: 960px; height: 1200px; }
  .card {
    position: absolute;
    left: 73px;
    width: 814px;
    height: 465px;
    border: 2px solid var(--card-edge);
    background: var(--paper);
    overflow: hidden;
  }
  .card--front { top: 63px; }
  .card--back { top: 670px; }

  /* Front */
  .brand-square {
    position: absolute;
    left: 347px;
    top: 100px;
    width: 120px;
    height: 120px;
    background: var(--brand-green);
  }
  .wordmark {
    position: absolute;
    left: 0;
    right: 0;
    top: 292px;
    text-align: center;
    font-weight: 400;
    color: var(--ink);
  }
  .wordmark__name {
    display: block;
    font-size: 38px;
    letter-spacing: 0.04em;
    line-height: 1;
    text-transform: uppercase;
  }
  .wordmark__descriptor {
    display: block;
    margin-top: 20px;
    font-size: 19px;
    letter-spacing: 0.62em;
    padding-left: 0.62em;
    line-height: 1;
    text-transform: uppercase;
  }

  /* Back */
  .rep-name {
    position: absolute;
    left: 57px;
    top: 52px;
    font-size: 35px;
    font-weight: 400;
    letter-spacing: 0.01em;
  }
  .contact {
    position: absolute;
    left: 58px;
    top: 318px;
    list-style: none;
    font-size: 19px;
    font-weight: 400;
    line-height: 33px;
    letter-spacing: 0.01em;
  }
  .back-mark {
    position: absolute;
    left: 508px;
    top: 80px;
    width: 230px;
    height: 230px;
    background: var(--brand-green);
  }
  .back-name {
    position: absolute;
    left: 508px;
    top: 334px;
    width: 230px;
    text-align: center;
    font-size: 18px;
    font-weight: 400;
    letter-spacing: 0.06em;
    text-transform: uppercase;
    color: var(--ink);
  }
</style>
</head>
<body>
  <main class="sheet">
    <section class="card card--front" aria-label="Card front">
      <div class="brand-square"></div>
      <h1 class="wordmark">
        <span class="wordmark__name">Harborline Crest</span>
        <span class="wordmark__descriptor">Consulting</span>
      </h1>
    </section>

    <section class="card card--back" aria-label="Card back">
      <h2 class="rep-name">Peter Vance</h2>
      <ul class="contact">
        <li>833-555-0172</li>
        <li>pvance@harborlinecrest.com</li>
        <li>www.harborlinecrest.com</li>
      </ul>
      <div class="back-mark"></div>
      <p class="back-name">Harborline Crest</p>
    </section>
  </main>
</body>
</html>
```